Photography Prints Business Card Design

Background info: Nature, flower, landscape,  macro, wildlife photographer. Shoot color and B&W images. Sell prints at juried fine art shows.
Looking for two-sided, clean, memorable design with creative use of my initials, DK.   I like the DK symbol in the my logo. Just use the DK symbol. Do not leave the underlying text as uploaded by me. I do not like the serif font and positioning of the words!  Either  remove the small print "Dorian Kessler Photography" under the logo,  or change to a sans serif font, or reposition with "Dorian Kessler" above "Photography" which seems to work with serif fonts.
Target Market(s)
Sophisticated art buyers, post-college to middle age
Industry/Entity Type
Business
Contact Information for Business Card
Dorian Kessler Photography
842 Harrow Bend CT
Marlowe Ridge, NC 28914
(336) 555-0148
www.doriankessler.com
PW:kesslerphoto
dorian@doriankessler.com
If using just one line address, make sure there is a comma after  "CT" in street address. For example:
842 Harrow Bend CT, Marlowe Ridge, NC 28914
Requirements
Must have
- 1.Two-sided card submitted as one design.
2. Must use the DK symbol in my logo.
3. Do not leave the text "Dorian Kessler Photography" under the DK symbol in the logo uploaded by me. I do not like that serif font or the positioning of the words! Either remove the small print "Dorian Kessler Photography" under the logo entirely, or change text to a sans serif font, or reposition text with "Dorian Kessler" above "Photography" which seems to work with serif fonts.
Nice to have
- Can use my DK logo (three file types uploaded: AI, PSD, TIF)  I  like the attached B&W water droplet photo.  My pictures on my website, www.doriankkessler.com  can also be used.  Possible use of Pinwave logo with (either the "f" alone or the square blue icon with white "f") my PW page short url name: kesslerphoto.
Should not have
- 1.No icons or pictures  of camera or lenses or other photographic gear or film strips.
2. No QR or other "barcode" type symbols.
3. No outlining of my logo symbol (drop shadow possibly).
4. No decorative or outlined fonts.
5. I am not a fan of most script fonts.
6. No play on "Kessler" such as snow or other winter season symbols.
7. Do not keep the original text, "Dorian Kessler Photography" under DK logo. Change it or remove it entirely.

```html
<!DOCTYPE html>
<html lang="en">
<head>
<meta charset="utf-8">
<title>Dorian Kessler Photography – Business Card</title>
<link rel="stylesheet" href="https://fonts.googleapis.com/css2?family=Barlow:wght@400;500&display=swap">
<style>
  :root {
    --backdrop: #3a3431;
    --card: #ffffff;
    --ink: #111111;
    --ink-soft: #2b2b2b;
    --rule: #555555;
  }
  * { margin: 0; padding: 0; box-sizing: border-box; }
  html, body {
    width: 1200px; height: 716px; overflow: hidden;
    background: var(--backdrop);
    font-family: "Barlow", Arial, sans-serif;
  }
  .canvas { position: relative; width: 1200px; height: 716px; }
  .card {
    position: absolute;
    width: 500px; height: 286px;
    background: var(--card);
    overflow: hidden;
    box-shadow: 0 10px 28px rgba(0,0,0,.45);
  }
  /* Front side: oversized cropped initials */
  .card--front { left: 60px; top: 215px; }
  .front-initials {
    position: absolute;
    left: -70px; top: -150px;
    font-weight: 500;
    font-size: 560px;
    line-height: 1;
    letter-spacing: -30px;
    color: var(--ink);
    white-space: nowrap;
  }
  /* Back side: contact details and initials mark */
  .card--back { left: 640px; top: 215px; }
  .identity {
    position: absolute; left: 44px; top: 40px;
    color: var(--ink-soft);
  }
  .identity__name { font-size: 19px; font-weight: 400; line-height: 1.1; }
  .identity__trade { font-size: 12px; line-height: 1.2; }
  .contact {
    position: absolute; left: 38px; top: 112px;
    padding-left: 14px;
    border-left: 1.5px solid var(--rule);
    list-style: none;
    font-size: 15px;
    line-height: 1.5;
    color: var(--ink-soft);
    white-space: nowrap;
  }
  .mark {
    position: absolute; right: 44px; top: 96px;
  }
  .mark__initials {
    font-size: 78px; font-weight: 500; line-height: 1;
    color: var(--ink); letter-spacing: -2px;
  }
</style>
</head>
<body>
<main class="canvas">
  <section class="card card--front" aria-label="Card front">
    <span class="front-initials">DK</span>
  </section>

  <section class="card card--back" aria-label="Card back">
    <header class="identity">
      <p class="identity__name">Dorian Kessler</p>
      <p class="identity__trade">Photography</p>
    </header>
    <ul class="contact">
      <li>842 Harrow Bend CT<br>Marlowe Ridge, NC 28914</li>
      <li>(336) 555-0148</li>
      <li>www.doriankessler.com</li>
      <li>PW:kesslerphoto</li>
      <li>dorian@doriankessler.com</li>
    </ul>
    <div class="mark">
      <span class="mark__initials">DK</span>
    </div>
  </section>
</main>
</body>
</html>
```